Company service wheel graphic

A graphic demonstrating all the services the company offers.
I have hand drawn and written up on the attached the content that is required. Also attached is our company logo so you have a sense of the colour scheme of the logo.
This will eventually go into a company brochure, be used on our website etc.

Target Market(s)

Local GOvernment and other professionals who work in the sport, recreation and leisure industries

Industry/Entity Type

Sports, recreation, leisure, aquatics

Font styles to use
Other font styles liked:
• Calibri

Colors
0054AA
0677BA
7BADD7
CADEEF
E8F1F8

Requirements
Must have
• An eye catching graphic that captures all the information in the hand drawn atachement.
Nice to have
• Each quadrant in the circle to have its own colour, that links to the company logo

```html
<!DOCTYPE html>
<html lang="en">
<head>
<meta charset="utf-8">
<title>Service Wheel</title>
<link href="https://fonts.googleapis.com/css2?family=Montserrat:wght@500;600;800;900&display=swap" rel="stylesheet">
<style>
  :root{
    --navy:#29265b;
    --blue:#0677BA;
    --deep-blue:#0054AA;
    --accent:#5ec4e8;
    --q-plan:#dceef5;
    --q-manage:#c7e4f2;
    --q-grow:#bcd9e6;
    --q-impact:#acdcef;
    --white:#ffffff;
  }
  html,body{margin:0;padding:0;width:1200px;height:1200px;overflow:hidden;background:var(--white);}
  .wheel{position:relative;width:1200px;height:1200px;font-family:"Montserrat",Arial,sans-serif;color:var(--navy);}
  .wheel-art{position:absolute;inset:0;}
  .audience{font-family:"Montserrat",Arial,sans-serif;font-weight:500;font-size:32px;fill:var(--navy);}
  .audience .divider{fill:var(--accent);}
  .service-list{position:absolute;margin:0;padding:0;list-style:none;font-size:15px;font-weight:500;line-height:22px;}
  .service-list li{position:relative;padding-left:23px;}
  .service-list li::before{
    content:"";position:absolute;left:0;top:4px;width:11px;height:11px;border:1.5px solid var(--blue);border-radius:50%;
  }
  .service-list li::after{
    content:"\2192";position:absolute;left:2px;top:0;font-size:10px;line-height:21px;width:11px;text-align:center;color:var(--blue);font-weight:800;
  }
  .list-planning{left:289px;top:258px;}
  .list-management{left:617px;top:189px;}
  .list-growing{left:289px;top:804px;}
  .list-impact{left:617px;top:804px;}
  .banner{position:absolute;height:35px;display:flex;align-items:center;justify-content:center;color:var(--white);font-weight:800;font-size:14px;letter-spacing:1.4px;}
  .banner-facilities{left:359px;top:407px;width:482px;}
  .banner-activation{left:359px;top:757px;width:482px;}
  .banner svg{position:absolute;inset:0;z-index:0;}
  .banner span{position:relative;z-index:1;}
  .pillar{position:absolute;width:220px;text-align:center;font-weight:900;font-size:13.5px;letter-spacing:1.6px;line-height:16px;}
  .pillar svg{display:block;margin:0 auto 8px;}
  .pillar-planning{left:258px;top:470px;}
  .pillar-management{left:721px;top:470px;}
  .pillar-growing{left:258px;top:626px;}
  .pillar-impact{left:721px;top:632px;}
  .hub-title{position:absolute;left:452px;top:568px;width:292px;margin:0;text-align:center;font-weight:900;font-size:21px;letter-spacing:1.6px;line-height:22.5px;}
  .hub-title .lead{color:var(--blue);}
</style>
</head>
<body>
<main class="wheel">
  <svg class="wheel-art" width="1200" height="1200" viewBox="0 0 1200 1200">
    <defs>
      <clipPath id="wheel-clip"><circle cx="600" cy="600" r="497"/></clipPath>
      <path id="arc-top" d="M121,426 A510,510 0 0 1 1079,426"/>
      <path id="arc-bottom" d="M70,497 A540,540 0 1 0 1130,497"/>
    </defs>
    <g class="quadrants" clip-path="url(#wheel-clip)">
      <rect x="100" y="100" width="500" height="500" fill="var(--q-plan)"/>
      <rect x="600" y="100" width="500" height="500" fill="var(--q-manage)"/>
      <rect x="100" y="600" width="500" height="500" fill="var(--q-grow)"/>
      <rect x="600" y="600" width="500" height="500" fill="var(--q-impact)"/>
    </g>
    <text class="audience"><textPath href="#arc-top" startOffset="0" textLength="1240" lengthAdjust="spacing">LOCAL &amp; STAGE GOVERNMENT <tspan class="divider">|</tspan> SPORT &amp; LEISURE FACILITY MANAGERS</textPath></text>
    <text class="audience"><textPath href="#arc-bottom" startOffset="0" textLength="1895" lengthAdjust="spacing">INVESTORS <tspan class="divider">|</tspan> DEVELOPERS, ARCHITECTS &amp; DESIGNERS <tspan class="divider">|</tspan> SPORT, RECREATION &amp; COMMUNITY PROVIDERS</textPath></text>
    <circle class="hub" cx="598" cy="603" r="146" fill="var(--white)" stroke="var(--navy)" stroke-width="3"/>
  </svg>

  <ul class="service-list list-planning">
    <li>Feasibility studies</li>
    <li>Community &amp; stakeholder research</li>
    <li>Sport &amp; recreation strategies</li>
    <li>Design strategies</li>
    <li>Indoor &amp; outdoor spaces</li>
  </ul>
  <ul class="service-list list-management">
    <li>Activating underutilised assets</li>
    <li>Income &amp; revenue generation<br>strategies</li>
    <li>Mystery shopper &amp; business<br>health check</li>
    <li>Financial &amp; funding strategies</li>
    <li>Management support</li>
    <li>Business planning</li>
  </ul>
  <ul class="service-list list-growing">
    <li>Trends &amp; insights</li>
    <li>Health profiling</li>
    <li>Active recreation strategies</li>
    <li>Community program development</li>
    <li>Physical activity strategies</li>
    <li>Specific cohort strategies</li>
    <li>Sport &amp; program specific strategies</li>
  </ul>
  <ul class="service-list list-impact">
    <li>Community impact monitoring</li>
    <li>Social value</li>
    <li>Community outcomes &amp; KPIs</li>
    <li>Contract monitoring</li>
  </ul>

  <div class="banner banner-facilities">
    <svg width="482" height="35" viewBox="0 0 482 35"><polygon points="0,0 459,0 482,17.5 459,35 0,35 23,17.5" fill="var(--navy)"/></svg>
    <span>Community, Aquatic &amp; Recreation Facilities</span>
  </div>
  <div class="banner banner-activation">
    <svg width="482" height="35" viewBox="0 0 482 35"><polygon points="23,0 482,0 459,17.5 482,35 23,35 0,17.5" fill="var(--navy)"/></svg>
    <span>Community Activation</span>
  </div>

  <div class="pillar pillar-planning">
    <svg width="56" height="56" viewBox="0 0 56 56" fill="none" stroke="var(--blue)" stroke-width="2.2">
      <path d="M20 44h14M21 49h12M22 44v-6c-5-3-8-8-8-13a13 13 0 0 1 26 0c0 5-3 10-8 13v6"/>
      <circle cx="33" cy="20" r="5"/>
      <path d="M33 10v4M33 26v4M23 20h4M39 20h4"/>
    </svg>
    PLANNING
  </div>
  <div class="pillar pillar-management">
    <svg width="56" height="56" viewBox="0 0 56 56" fill="none" stroke="var(--blue)" stroke-width="2.2">
      <circle cx="28" cy="28" r="19"/>
      <path d="M28 3v6M28 47v6M3 28h6M47 28h6M10 10l4 4M42 42l4 4M46 10l-4 4M14 42l-4 4"/>
      <circle cx="22" cy="25" r="3"/><circle cx="34" cy="25" r="3"/><circle cx="28" cy="23" r="3"/>
      <path d="M18 35c0-4 20-4 20 0"/>
    </svg>
    MANAGEMENT
  </div>
  <div class="pillar pillar-growing">
    <svg width="56" height="56" viewBox="0 0 56 56" fill="none" stroke="var(--blue)" stroke-width="2.2">
      <rect x="6" y="38" width="7" height="14"/><rect x="18" y="32" width="7" height="20"/>
      <rect x="30" y="36" width="7" height="16"/><rect x="42" y="24" width="7" height="28"/>
      <path d="M4 26l12-12 10 8L46 6M38 6h8v8"/>
    </svg>
    GROWING<br>PARTICIPATION
  </div>
  <div class="pillar pillar-impact">
    <svg width="50" height="50" viewBox="0 0 50 50" fill="none" stroke="var(--blue)" stroke-width="2.2">
      <rect x="4" y="4" width="18" height="18" rx="3"/><rect x="28" y="4" width="18" height="18" rx="3"/>
      <rect x="4" y="28" width="18" height="18" rx="3"/><rect x="28" y="28" width="18" height="18" rx="3"/>
    </svg>
    COMMUNITY<br>IMPACT &amp; OUTCOMES
  </div>

  <h1 class="hub-title"><span class="lead">COMMUNITY &amp;</span><br>STAKEHOLDER<br>ENGAGEMENT</h1>
</main>
</body>
</html>
```